A4 Flier to send to Schools about Manners for School Students

We are expanding and now working with corporate clients as well as teaching etiquette and manners to High School students. This is a the flier we need created. The clients are Assistant Principals and Heads of School so we need to appear professional, approachable and aspirational and fun.
Here is the content and some images that may be useful to get started.

Target Market(s)

Assistant Principals and School Heads

Industry/Entity Type

School

Font styles to use
Sans Serif

Colors
00a990
ffffff

Requirements
Must have
• Cool pictures of young people - pref a mix of Asians, caucasians. Well dressed and happy teens and positive images.
• Logo
• Some use of green and white as this is our corporate style.
• Image of Clara Pendry
• Image of Ingrid Dowlatte
Nice to have
• I have put it all in the flier I have attached so please come back to me with any questions.
Should not have
• Any teens of African descent - only as Australian is mostly caucasian and Asian.
• Pinks

```html
<!DOCTYPE html>
<html lang="en">
<head>
<meta charset="utf-8">
<title>Etiquette &amp; Manners for Students</title>
<link href="https://fonts.googleapis.com/css2?family=Open+Sans:ital,wght@0,400;0,600;0,700;1,700&family=Roboto+Condensed:wght@400;700&display=swap" rel="stylesheet">
<style>
:root{
  --teal:#00a990;
  --teal-dark:#008a76;
  --ink:#3a3a3a;
  --grey:#6d6e70;
  --panel:#eeeeee;
  --band:#d9d9d9;
  --white:#ffffff;
}
*{margin:0;padding:0;box-sizing:border-box}
html,body{width:849px;height:1200px;overflow:hidden}
body{font-family:"Open Sans",Arial,sans-serif;color:var(--ink);background:var(--white)}
.flier{position:relative;width:849px;height:1200px;background:linear-gradient(180deg,#f4f4f4 0,#ffffff 40%,#ffffff 100%);overflow:hidden}
.hero-photo{position:absolute;left:0;top:0;width:700px;height:372px;background:linear-gradient(160deg,#d9d4cc 0%,#b89a82 45%,#6f7b86 100%)}
.brand{position:absolute;right:34px;top:30px;display:flex;align-items:center;gap:10px;font-weight:700;font-size:22px;color:var(--teal);line-height:1.05;text-align:right}
.brand-mark{width:16px;height:16px;border-radius:50%;background:var(--teal)}
.title-band{position:absolute;left:0;top:370px;width:440px}
.title-main{background:var(--teal);color:var(--white);font-family:"Roboto Condensed",Arial,sans-serif;font-weight:700;font-size:30px;padding:8px 0 8px 40px;letter-spacing:.5px}
.title-sub{background:var(--band);color:var(--ink);font-family:"Roboto Condensed",Arial,sans-serif;font-size:28px;padding:4px 0 6px 40px;width:300px}
.intro{position:absolute;left:40px;top:466px;width:420px}
.intro h2{color:var(--teal);font-size:20px;line-height:1.25;font-weight:700;margin-bottom:10px}
.intro p{font-size:13.5px;line-height:1.45;color:var(--grey)}
.topics{position:absolute;left:30px;top:676px;width:310px}
.topics-label{display:inline-block;background:var(--teal);color:var(--white);font-weight:700;font-size:16px;padding:4px 14px}
.topics ul{list-style:none;background:var(--panel)}
.topics li{font-family:"Roboto Condensed",Arial,sans-serif;font-weight:700;font-size:17.5px;line-height:1.2;padding:9px 12px;border-bottom:2px dashed var(--band)}
.topics li::before{content:"• ";color:var(--teal)}
.topics li.alt{background:var(--teal);color:var(--white);border-bottom-color:var(--teal)}
.topics li.alt::before{color:var(--white)}
.student-photo{position:absolute;left:318px;top:800px;width:180px;height:340px;background:linear-gradient(180deg,#c7a78d 0%,#5c6c7c 55%,#2f3c4a 100%)}
.pricing{position:absolute;left:488px;top:466px;width:340px;background:var(--teal);color:var(--white);text-align:center;padding:8px 10px}
.pricing p{font-size:17px;font-weight:700;line-height:1.35}
.pricing .tag{display:block;margin:6px auto 0;background:var(--white);color:var(--teal);font-size:16px;padding:3px 0;width:230px}
.agenda{position:absolute;left:488px;top:556px;width:340px;height:484px;background:var(--panel);padding:10px 14px;font-size:12.5px;line-height:1.4}
.agenda h3{color:var(--teal);font-style:italic;font-size:14px;margin-top:8px}
.agenda h3.bar{background:var(--teal);color:var(--white);font-style:normal;padding:2px 8px;margin:10px -14px 4px;font-size:14px}
.agenda ul{list-style:none;padding-left:10px}
.agenda li::before{content:"• ";color:var(--teal)}
.included{position:absolute;left:508px;top:1040px;width:320px;background:var(--teal);color:var(--white);padding:8px 14px;font-size:12.5px;line-height:1.4}
.included h4{font-size:14px;margin-bottom:2px}
.included ul{list-style:none}
.included li::before{content:"• "}
.footer{position:absolute;left:0;bottom:0;width:849px;height:52px;background:var(--grey);color:var(--white);font-size:16px;display:flex;align-items:center;padding-left:40px}
</style>
</head>
<body>
<div class="flier">
  <div class="hero-photo" role="img" aria-label="Group of smiling, well-dressed teenagers holding books"></div>
  <div class="brand"><span class="brand-mark"></span><span>The Fine Graces<br>Company</span></div>

  <div class="title-band">
    <div class="title-main">ETIQUETTE &amp; MANNERS</div>
    <div class="title-sub">FOR STUDENTS</div>
  </div>

  <section class="intro">
    <h2>Are you frustrated by the lack of manners and courtesy shown by students today?</h2>
    <p>Reports show that students are applying for jobs lacking social skills and etiquette, making them unprepared for part time jobs and full time workplaces. The sooner they learn good habits around manners and etiquette, the more well-rounded and prepared they will be for leadership opportunities, employment and forming good relationships.</p>
  </section>

  <section class="topics">
    <span class="topics-label">Topics</span>
    <ul>
      <li>Modern manners for young people</li>
      <li class="alt">How to introduce and others yourself correctly</li>
      <li>Job Interview Preparation</li>
      <li class="alt">Formal Preparation</li>
      <li>Netiquette, conduct with mobiles, devices and social media</li>
      <li class="alt">Table Manners</li>
      <li>Department, how to walk, sit, carry yourself with poise and confidence</li>
      <li class="alt">Dating Etiquette</li>
    </ul>
  </section>

  <div class="student-photo" role="img" aria-label="Smiling student holding colourful folders"></div>

  <section class="pricing">
    <p>Prices from<br>$500 for 1 hour to $1500 for day</p>
    <span class="tag">Sample one hour agenda</span>
  </section>

  <section class="agenda">
    <h3>Introduction</h3>
    <ul><li>What are good vs bad manners?</li><li>Why it is important today?</li></ul>
    <h3>The Rules</h3>
    <ul><li>Appropriate conduct for young ladies and gentlemen</li></ul>
    <h3 class="bar">The First Impression</h3>
    <ul>
      <li>How to make a good first impression</li>
      <li>Speaking clearly</li>
      <li>What to wear, when and when, dressing appropriately for the occasion</li>
      <li>What not to wear, where and when incl job interviews</li>
    </ul>
    <h3 class="bar">Introductions</h3>
    <ul>
      <li>How to introduce yourself correctly</li>
      <li>How to introduce one person to another</li>
      <li>Handshaking skills</li>
      <li>Putting it all together</li>
    </ul>
  </section>

  <section class="included">
    <h4>What's Included...</h4>
    <ul>
      <li>Handout to take home to parents</li>
      <li>Classroom Poster</li>
      <li>copy of "Poise Pointers" Book for School</li>
    </ul>
  </section>

  <footer class="footer">www.finegraces.com.au</footer>
</div>
</body>
</html>
```